Bus tour company needs and new look for their brochure design

We already have a brochure designed using Printwell, but its very busy and we haven't had many tour booking from the brochures we have displayed out there.
Heart of the Baronvale provides a variety of specialised tours that feature world class experiences that showcase the Fleurieu region’s (South Australia) culture, heritage, food and wine in an unspoilt natural environment. We would really like the brochure to have great images, some of which I have and some I dont. It needs to grab people attention when displayed amongst many others. We have a logo already and our bus has also been signed with the logo.
Our website is www.hbjourneys.com.au if you would like to have a look at what we do and how the site looks. I am not to fussed that the brochure look and feel the same as the website, just that it has a similar feel to the logo and our products we offer.

I would like to remove the Calloway Lane tour product from the brochure and add a different food and wine tour. I can provide this information when needed.
Updates

HI all designers I have added so logo images without the white background. Could you please try this logo option on your designs?

Target Market(s)

Activity Seekers – mix of young singles and older people (45+) often
travelling in groups of friends and more likely to be male.

The Savour and Unwind Segment are more likely to be females aged
over 50 travelling with a partner or female friends.. They like
to indulge in little luxuries and special treats. great for regional food and wine tours.

Family Focussed – predominantly midlife families looking to spend quality
time and reconnect with partners and children.

Industry/Entity Type

It Company

Font styles to use
Serif
Sans Serif

Colors
3176b5
00a990
33a6d7
85cae6
000000
ffffff
9bcb3c
fbed22

Requirements
Must have
• Must have contact details; 0471 582 914
• book now www.hbjourneys.com.au
• great images
• logo
• reference to location: Fleurieu Peninsula, South Australia
Should not have
• too much detail in the products.

```html
<!DOCTYPE html>
<html lang="en">
<head>
<meta charset="utf-8">
<title>Discover the Fleurieu Tour – Brochure Concepts</title>
<link href="https://fonts.googleapis.com/css2?family=Bebas+Neue&family=Great+Vibes&family=Lato:ital,wght@0,400;0,700;1,400&family=Open+Sans:wght@800&display=swap" rel="stylesheet">
<style>
  :root{
    --board:#0f2226;
    --board-text:#a9b3b5;
    --sun:#f9b51c;
    --lemon:#fbed22;
    --ocean:#3a78b8;
    --sky:#85cae6;
    --navy:#14184a;
    --teal:#1b4b63;
    --ink:#000;
    --paper:#fff;
    --slate:#3b3b45;
    --lime:#c6e04a;
    --grey-strip:#6f7075;
  }
  *{box-sizing:border-box;margin:0;padding:0}
  html,body{width:1200px;height:1200px;overflow:hidden;background:var(--board)}
  .board{position:relative;width:1200px;height:1200px;background:var(--board);font-family:'Lato',sans-serif}
  .board-title{position:absolute;top:12px;left:0;width:100%;text-align:center;font-family:'Bebas Neue',sans-serif;font-size:48px;color:var(--board-text);letter-spacing:1px}
  .board-note{position:absolute;top:66px;left:0;width:100%;text-align:center;font-family:'Bebas Neue',sans-serif;font-size:19px;color:var(--board-text)}

  .flyer{position:absolute;overflow:hidden;background:var(--ocean)}
  .flyer--blue{left:80px;top:104px;width:478px;height:1072px}
  .flyer--sun{left:617px;top:98px;width:488px;height:1078px}

  .flyer__header{position:absolute;left:0;top:0;width:100%;height:128px;background:var(--sun)}
  .flyer__kicker{position:absolute;left:4%;top:34px;font-family:'Bebas Neue',sans-serif;font-size:23px;line-height:1;color:#ececec;text-shadow:2px 2px 3px rgba(0,0,0,.45)}
  .flyer__title{position:absolute;left:4%;top:58px;font-family:'Bebas Neue',sans-serif;font-size:60px;line-height:1;color:#ececec;text-shadow:3px 3px 4px rgba(0,0,0,.5)}
  .brand{position:absolute;right:4%;top:36px;width:128px;display:flex;align-items:center;gap:8px}
  .brand__name{font-family:'Bebas Neue',sans-serif;font-size:24px;line-height:.95;color:var(--paper);text-align:right}
  .brand__dot{flex:none;width:24px;height:24px;border-radius:50%;background:var(--ocean)}

  .flyer__hero{position:absolute;left:0;top:128px;width:100%;height:272px;
    background:linear-gradient(180deg,#2f6fb0 0%,#3a86c8 6%,#3f8e3a 12%,#2f9a2c 35%,#d7b321 55%,#2e8f2a 70%,#1f6d1e 100%)}
  .flyer__strip{position:absolute;left:0;top:400px;width:100%;height:10px;background:var(--grey-strip)}
  .flyer__band{position:absolute;left:0;top:410px;width:100%;height:290px;background:var(--ocean)}
  .flyer--sun .flyer__band{background:var(--lemon)}

  .photo{position:absolute;border:6px solid var(--paper);box-shadow:2px 3px 6px rgba(0,0,0,.45)}
  .photo--jetty{left:2.1%;width:30.6%;height:108px;background:linear-gradient(180deg,#1f5db0 0%,#9cc7ee 45%,#2e9fb4 75%,#1b3a40 100%)}
  .photo--cliff{left:34.3%;width:30.6%;height:108px;background:linear-gradient(160deg,#6e6a5a 0%,#8d8672 45%,#d9e2e6 70%,#b7b1a0 100%)}
  .photo--roo{left:66.7%;width:30.6%;height:108px;background:linear-gradient(180deg,#1c7db0 0%,#3ba4cf 55%,#a77a4a 80%,#6b6a3a 100%)}
  .photo--walk{left:66.7%;width:30.6%;height:108px;background:linear-gradient(170deg,#a9b37f 0%,#6f8f4a 40%,#1f63a8 70%,#2a5e2a 100%)}
  .photo--map{left:66.7%;width:30.6%;height:108px;background:linear-gradient(150deg,#eef0e6 0%,#e4e6d6 50%,#a9cdeb 70%,#9cc4e8 100%)}
  .flyer--blue .photo--jetty,.flyer--blue .photo--cliff,.flyer--blue .photo--roo{top:348px}
  .flyer--blue .photo--walk{top:468px}
  .flyer--blue .photo--map{top:589px}
  .flyer--sun .photo--jetty,.flyer--sun .photo--cliff,.flyer--sun .photo--roo{top:350px}
  .flyer--sun .photo--walk{top:470px}
  .flyer--sun .photo--map{top:591px}

  .includes{position:absolute;left:2.5%;top:466px;width:61.7%;height:234px;background:var(--sky);padding:6px 10px 0 12px;color:var(--slate)}
  .flyer--sun .includes{top:468px;background:var(--ocean);color:var(--paper)}
  .script{font-family:'Great Vibes',cursive;font-size:25px;text-align:center;line-height:1.1;font-weight:400}
  .includes .script{color:var(--navy);margin-bottom:4px}
  .flyer--sun .includes .script{color:var(--paper)}

  .checklist{list-style:none;font-size:10.3px;line-height:1.2}
  .checklist li{position:relative;padding-left:20px;margin-bottom:3.6px}
  .checklist li::before{content:"✓";position:absolute;left:2px;top:0;font-weight:700}

  .highlights-head{position:absolute;left:0;top:700px;width:100%;height:38px;background:var(--navy);padding-top:2px}
  .flyer--sun .highlights-head{top:702px;background:var(--ink)}
  .highlights-head .script{color:var(--sun)}
  .highlights{position:absolute;left:0;top:738px;width:100%;height:164px;background:var(--ocean);padding:6px 14px 0 28px;color:var(--paper)}
  .flyer--sun .highlights{top:740px;background:var(--lemon);color:var(--ink)}
  .highlights .checklist li{margin-bottom:4px}
  .disclaimer{font-style:italic;font-size:10px;line-height:1.25;color:var(--lime);margin:6px 0 0 -16px}
  .flyer--sun .disclaimer{color:var(--ink)}

  .book{position:absolute;left:0;top:902px;width:100%;height:46px;background:var(--paper)}
  .flyer--sun .book{top:904px}
  .book__text{position:absolute;left:5%;top:2px;font-family:'Open Sans',sans-serif;font-weight:800;font-size:30px;color:var(--slate);letter-spacing:.5px}
  .book__van{position:absolute;right:1%;top:2px;width:19%;height:42px;background:linear-gradient(180deg,#9fb7c6 0%,#eef2f4 40%,#d9dde0 70%,#6c6f72 100%)}

  .call{position:absolute;left:0;top:948px;width:100%;height:58px;background:var(--lemon);display:flex;align-items:center;padding-left:6%;gap:10px;color:var(--ink)}
  .flyer--sun .call{top:950px;background:var(--ink);color:var(--paper)}
  .call__label,.call__number{font-family:'Bebas Neue',sans-serif;line-height:1;white-space:nowrap}
  .call__label{font-size:38px;word-spacing:3px}
  .call__number{font-size:42px;letter-spacing:.5px}
  .call__icon{width:40px;height:40px;flex:none}

  .web{position:absolute;left:0;top:1006px;width:100%;height:66px;background:var(--teal);display:flex;align-items:center;padding-left:7%;gap:18px}
  .flyer--sun .web{top:1008px;height:70px}
  .web__icon{width:40px;height:40px;flex:none}
  .web__url{font-family:'Bebas Neue',sans-serif;font-size:42px;color:var(--paper);line-height:1;white-space:nowrap}
</style>
</head>
<body>
<main class="board">
  <h1 class="board-title">Design Idea - 02</h1>
  <p class="board-note">(Colors, fonts &amp; placements are changeable)</p>

  <article class="flyer flyer--blue">
    <header class="flyer__header">
      <p class="flyer__kicker">Discover the</p>
      <h2 class="flyer__title">Fleurieu Tour</h2>
      <div class="brand"><span class="brand__name">Heart of the Baronvale</span><span class="brand__dot"></span></div>
    </header>
    <div class="flyer__hero" role="img" aria-label="Aerial view of green vineyard rows across rolling hills with the sea on the horizon"></div>
    <div class="flyer__strip"></div>
    <div class="flyer__band"></div>
    <div class="photo photo--jetty" role="img" aria-label="Long timber jetty over turquoise water under a cloudy blue sky"></div>
    <div class="photo photo--cliff" role="img" aria-label="Rocky coastal headland with waves breaking on the shore"></div>
    <div class="photo photo--roo" role="img" aria-label="Kangaroo leaping across a grassy hilltop against blue sky"></div>
    <section class="includes">
      <h3 class="script">Full Day Tour Includes</h3>
      <ul class="checklist">
        <li>Professional &amp; friendly driver guide.</li>
        <li>Comfortable, safe and reliable vehicle.</li>
        <li>All park entrance fees.</li>
        <li>All meals including morning tea, gourmet picnic lunch and cheese platter.</li>
        <li>Wine tasting.</li>
        <li>Pick up and return from selected accommodation is available at no extra cost.</li>
        <li>Departs 8:00am.</li>
        <li>Returns approximately 5.00pm.</li>
        <li>Cost per person $185 adults, $135 children (4-16years) includes morning tea, lunch and cheese platter. Minimum 2 people</li>
      </ul>
    </section>
    <div class="photo photo--walk" role="img" aria-label="Group of walkers on a coastal hill path above a blue bay"></div>
    <div class="photo photo--map" role="img" aria-label="Road map of the Fleurieu Peninsula with tour stops marked"></div>
    <div class="highlights-head"><h3 class="script">Tour Highlights</h3></div>
    <section class="highlights">
      <ul class="checklist">
        <li>An important South Australian landmark in Rapid Bay.</li>
        <li>A guided walk through Deep Creek Conservation Park.</li>
        <li>The largest remaining block of wildlife habitat on the Fleurieu Peninsula.</li>
        <li>Enjoy a gourmet picnic lunch besides some local kangaroos and bird-life before visiting the historic seaside town of Victor Harbor where you will discover some of the local Indigenous heritage, early settlement and whaling history.</li>
        <li>Enjoy some great photo opportunities of Encounter Bay, the Bluff and Granite Island.</li>
        <li>Then wind down with a glass of wine and gourmet cheese platter and at local winery.</li>
      </ul>
      <p class="disclaimer">All locations and suggested places to visit are subject to change. There is a minimum of 2 persons required for all tour departures.</p>
    </section>
    <div class="book">
      <p class="book__text">Book Your Tour Now</p>
      <div class="book__van" role="img" aria-label="White tour minibus"></div>
    </div>
    <div class="call">
      <span class="call__label">Call us now</span>
      <svg class="call__icon" viewBox="0 0 44 44" aria-hidden="true"><circle cx="22" cy="22" r="19.5" fill="none" stroke="currentColor" stroke-width="4"/><path d="M15 12c2-1 3 0 4 3l1 3c0 2-2 2-2 3 1 3 3 5 6 6 1 0 1-2 3-2l3 1c3 1 4 2 3 4-1 3-4 4-7 3-6-2-11-7-13-13-1-3 0-6 2-8z" fill="currentColor"/></svg>
      <span class="call__number">0471 582 914</span>
    </div>
    <div class="web">
      <svg class="web__icon" viewBox="0 0 42 42" aria-hidden="true" fill="none" stroke="#cfd6d9" stroke-width="2.4"><circle cx="21" cy="21" r="18.5"/><ellipse cx="21" cy="21" rx="8" ry="18.5"/><path d="M2.5 21h37M5 12h32M5 30h32M21 2.5v37"/></svg>
      <span class="web__url">www.hbjourneys.com.au</span>
    </div>
  </article>

  <article class="flyer flyer--sun">
    <header class="flyer__header">
      <p class="flyer__kicker">Discover the</p>
      <h2 class="flyer__title">Fleurieu Tour</h2>
      <div class="brand"><span class="brand__name">Heart of the Baronvale</span><span class="brand__dot"></span></div>
    </header>
    <div class="flyer__hero" role="img" aria-label="Aerial view of green vineyard rows across rolling hills with the sea on the horizon"></div>
    <div class="flyer__strip"></div>
    <div class="flyer__band"></div>
    <div class="photo photo--jetty" role="img" aria-label="Long timber jetty over turquoise water under a cloudy blue sky"></div>
    <div class="photo photo--cliff" role="img" aria-label="Rocky coastal headland with waves breaking on the shore"></div>
    <div class="photo photo--roo" role="img" aria-label="Kangaroo leaping across a grassy hilltop against blue sky"></div>
    <section class="includes">
      <h3 class="script">Full Day Tour Includes</h3>
      <ul class="checklist">
        <li>Professional &amp; friendly driver guide.</li>
        <li>Comfortable, safe and reliable vehicle.</li>
        <li>All park entrance fees.</li>
        <li>All meals including morning tea, gourmet picnic lunch and cheese platter.</li>
        <li>Wine tasting.</li>
        <li>Pick up and return from selected accommodation is available at no extra cost.</li>
        <li>Departs 8:00am.</li>
        <li>Returns approximately 5.00pm.</li>
        <li>Cost per person $185 adults, $135 children (4-16years) includes morning tea, lunch and cheese platter. Minimum 2 people</li>
      </ul>
    </section>
    <div class="photo photo--walk" role="img" aria-label="Group of walkers on a coastal hill path above a blue bay"></div>
    <div class="photo photo--map" role="img" aria-label="Road map of the Fleurieu Peninsula with tour stops marked"></div>
    <div class="highlights-head"><h3 class="script">Tour Highlights</h3></div>
    <section class="highlights">
      <ul class="checklist">
        <li>An important South Australian landmark in Rapid Bay.</li>
        <li>A guided walk through Deep Creek Conservation Park.</li>
        <li>The largest remaining block of wildlife habitat on the Fleurieu Peninsula.</li>
        <li>Enjoy a gourmet picnic lunch besides some local kangaroos and bird-life before visiting the historic seaside town of Victor Harbor where you will discover some of the local Indigenous heritage, early settlement and whaling history.</li>
        <li>Enjoy some great photo opportunities of Encounter Bay, the Bluff and Granite Island.</li>
        <li>Then wind down with a glass of wine and gourmet cheese platter and at local winery.</li>
      </ul>
      <p class="disclaimer">All locations and suggested places to visit are subject to change. There is a minimum of 2 persons required for all tour departures.</p>
    </section>
    <div class="book">
      <p class="book__text">Book Your Tour Now</p>
      <div class="book__van" role="img" aria-label="White tour minibus"></div>
    </div>
    <div class="call">
      <span class="call__label">Call us now</span>
      <svg class="call__icon" viewBox="0 0 44 44" aria-hidden="true"><circle cx="22" cy="22" r="19.5" fill="none" stroke="#8a8a8a" stroke-width="4"/><path d="M15 12c2-1 3 0 4 3l1 3c0 2-2 2-2 3 1 3 3 5 6 6 1 0 1-2 3-2l3 1c3 1 4 2 3 4-1 3-4 4-7 3-6-2-11-7-13-13-1-3 0-6 2-8z" fill="#8a8a8a"/></svg>
      <span class="call__number">0471 582 914</span>
    </div>
    <div class="web">
      <svg class="web__icon" viewBox="0 0 42 42" aria-hidden="true" fill="none" stroke="#cfd6d9" stroke-width="2.4"><circle cx="21" cy="21" r="18.5"/><ellipse cx="21" cy="21" rx="8" ry="18.5"/><path d="M2.5 21h37M5 12h32M5 30h32M21 2.5v37"/></svg>
      <span class="web__url">www.hbjourneys.com.au</span>
    </div>
  </article>
</main>
</body>
</html>
```